Business Cards for a start up company

We are looking for a business card design for a start up company based in Ohio. The logo is attached. We are a healthcare company. We are open to all designs but want something professional but fun; creative, not boring

Industry/Entity Type

Healthcare

```html
<!DOCTYPE html>
<html lang="en">
<head>
<meta charset="utf-8">
<title>Bright Bridge Care – Business Cards</title>
<link rel="stylesheet" href="https://fonts.googleapis.com/css2?family=Zilla+Slab:wght@700&display=swap">
<style>
  :root {
    --green: #86c13f;
    --navy: #24275e;
    --ink: #2a2326;
    --paper: #ffffff;
    --frame: #8a8a8a;
    --faint: rgba(150, 160, 190, 0.18);
    --page: #ffffff;
  }
  * { margin: 0; padding: 0; box-sizing: border-box; }
  html, body {
    width: 1200px; height: 338px; overflow: hidden; background: var(--page);
  }
  .sheet {
    position: relative; width: 1200px; height: 338px;
    display: flex; gap: 4px;
  }
  .card {
    position: relative; width: 598px; height: 338px;
    background: var(--paper); border: 1px solid var(--frame);
    overflow: hidden;
    font-family: "Zilla Slab", Georgia, serif; font-weight: 700;
  }
  .card-art { position: absolute; inset: 0; width: 100%; height: 100%; }
  .brand {
    position: absolute; display: flex; align-items: center;
    color: var(--navy); white-space: nowrap;
  }
  .brand-dot { border-radius: 50%; background: var(--navy); flex: none; }
  .brand--front { left: 42px; top: 98px; gap: 22px; font-size: 46px; }
  .brand--front .brand-dot { width: 112px; height: 112px; }
  .brand--back { left: 30px; top: 50px; gap: 16px; font-size: 30px; }
  .brand--back .brand-dot { width: 64px; height: 64px; }
  .contact-list {
    position: absolute; left: 30px; top: 264px; list-style: none;
    color: var(--ink); font-size: 16px; line-height: 27px;
  }
  .contact-list li { display: flex; align-items: center; gap: 8px; }
  .contact-icon {
    width: 18px; height: 18px; background: var(--green);
    border: 1px solid #fff; border-radius: 3px; flex: none;
  }
  .address {
    position: absolute; left: 32px; top: 220px;
    font-style: normal; color: var(--ink); font-size: 18px; line-height: 21px;
  }
</style>
</head>
<body>
<main class="sheet">
  <section class="card card--front">
    <svg class="card-art" viewBox="0 0 598 338" aria-hidden="true">
      <path d="M330 0 C430 10 520 60 598 150 L598 0 Z" fill="var(--green)"/>
      <path d="M0 205 C150 290 400 320 598 320 L598 338 L0 338 Z" fill="var(--green)"/>
      <circle cx="379" cy="150" r="115" fill="var(--faint)"/>
    </svg>
    <div class="brand brand--front">
      <span class="brand-dot"></span>
      <span class="brand-name">Bright Bridge Care</span>
    </div>
    <ul class="contact-list">
      <li>
        <svg class="contact-icon" viewBox="0 0 18 18" aria-hidden="true">
          <rect x="3.5" y="5" width="11" height="8" fill="none" stroke="#fff" stroke-width="1.4"/>
          <path d="M3.5 5 L9 10 L14.5 5" fill="none" stroke="#fff" stroke-width="1.4"/>
        </svg>
        danielreeve@brightbridgecare.com
      </li>
      <li>
        <svg class="contact-icon" viewBox="0 0 18 18" aria-hidden="true">
          <path d="M5 3.5 L7.5 3.5 L8.5 6.5 L7 7.8 C7.8 9.6 8.6 10.4 10.2 11 L11.5 9.5 L14.5 10.5 L14.5 13 C9 13.5 4.5 9 5 3.5 Z" fill="#fff"/>
        </svg>
        555-014-0200 ext 100
      </li>
    </ul>
  </section>

  <section class="card card--back">
    <svg class="card-art" viewBox="0 0 598 338" aria-hidden="true">
      <path d="M0 0 L0 40 C60 5 130 0 200 0 Z" fill="var(--green)"/>
      <path d="M190 0 C380 10 520 60 598 130 L598 0 Z" fill="var(--green)"/>
      <path d="M170 338 C330 330 480 300 598 240 L598 338 Z" fill="var(--green)"/>
      <circle cx="362" cy="160" r="115" fill="var(--faint)"/>
    </svg>
    <div class="brand brand--back">
      <span class="brand-dot"></span>
      <span class="brand-name">Bright Bridge Care</span>
    </div>
    <address class="address">
      Daniel Reeve<br>
      Chief Operating Officer<br>
      PO Box 417<br>
      Dayton, Ohio&nbsp; 45402
    </address>
  </section>
</main>
</body>
</html>
```